Rio Dorado Salsa – CPG Website with WordPress - Store Locator: WP Maps plugin

Larkmoor Food Company is a startup consumer packaged goods (CPG) brand launching its flagship product line — Rio Dorado Salsa. We’re seeking a talented web designer to create a bold, professional, mobile-optimized website using WordPress with a WP Maps store locator to help customers find local retailers.

Our goal is to build a strong online presence that supports both retail growth and direct-to-consumer sales.

See Rio Dorado _Website_Design_Brief word document.

The website URL is https://riodoradosalsa.example/

Target Market(s)

Consumers of gourmet salsa

Industry/Entity Type

Consumer Packaged Goods - Salsa manufacturer.

Coding

Coded - Design and coding required

Number of Pages Required

5+ page

Requirements
Must have
• The design of the Rio Dorado Salsa website shall emulate the clean, polished aesthetic of Brinvale.example.

```html
<!DOCTYPE html>
<html lang="en">
<head>
<meta charset="utf-8">
<title>Rio Dorado Salsa</title>
<link href="https://fonts.googleapis.com/css2?family=Oswald:wght@500;600&family=Poppins:wght@400;500&display=swap" rel="stylesheet">
<style>
:root{
  --red:#c8202a;
  --cream:#f6f0e6;
  --ink:#111111;
  --body:#2a2a2a;
  --muted:#555555;
  --white:#ffffff;
  --star:#f0a22a;
}
*{margin:0;padding:0;box-sizing:border-box}
html,body{width:1200px;height:3453px;overflow:hidden}
body{position:relative;background:var(--cream);font-family:"Poppins",sans-serif;color:var(--body)}
.abs{position:absolute}
.head-font{font-family:"Oswald",sans-serif;text-transform:uppercase}

.site-header{left:0;top:0;width:1200px;height:137px;background:var(--white);border-top:4px solid var(--red);z-index:2}
.brand{left:124px;top:36px;font-family:"Oswald",sans-serif;font-weight:600;font-size:44px;color:var(--red)}
.account{left:767px;top:30px;font-family:"Oswald",sans-serif;font-weight:500;font-size:17px;color:var(--ink);display:flex;align-items:center;gap:10px}
.order-btn{left:912px;top:14px;width:160px;height:51px;border-radius:26px;background:var(--red);color:var(--white);font-family:"Oswald",sans-serif;font-weight:500;font-size:18px;display:flex;align-items:center;justify-content:center;gap:8px}
.main-nav{left:398px;top:88px;display:flex;gap:44px;font-family:"Oswald",sans-serif;font-weight:500;font-size:17px;color:var(--ink)}
.main-nav .active{border-bottom:2px solid var(--red);padding-bottom:2px}

.hero{left:0;top:137px;width:1200px;height:720px;background:
  radial-gradient(ellipse 300px 200px at 200px 300px,rgba(120,140,70,.55),transparent),
  radial-gradient(ellipse 260px 180px at 1000px 250px,rgba(200,150,90,.5),transparent),
  radial-gradient(ellipse 200px 150px at 720px 400px,rgba(110,150,60,.45),transparent),
  linear-gradient(180deg,#4a3f35,#3a2f27 60%,#2b231d)}
.hero-shade{left:0;top:137px;width:1200px;height:720px;background:rgba(0,0,0,.18)}
.hero-fade{left:0;top:620px;width:1200px;height:300px}
.hero-kicker{left:0;top:212px;width:1200px;text-align:center;color:var(--white);font-size:35px;font-weight:500;line-height:1.2}
.hero-title{left:0;top:262px;width:1200px;text-align:center;color:var(--white);font-size:70px;font-weight:600;line-height:1.1}
.btn{background:var(--red);color:var(--white);border-radius:28px;font-family:"Oswald",sans-serif;font-weight:500;text-transform:uppercase;display:flex;align-items:center;justify-content:center}
.hero-btn{left:518px;top:360px;width:165px;height:53px;font-size:22px}
.chili{background:radial-gradient(ellipse at center,rgba(255,255,255,.9) 0%,rgba(255,255,255,.55) 55%,rgba(255,255,255,0) 72%)}
.chili-left{left:98px;top:300px;width:120px;height:92px;transform:rotate(35deg)}
.chili-right{left:935px;top:330px;width:90px;height:64px;transform:rotate(-50deg)}
.jar{border-radius:38px 38px 46px 46px;box-shadow:0 18px 24px rgba(0,0,0,.18)}
.jar-hot{left:330px;top:498px;width:200px;height:340px;background:linear-gradient(180deg,#d7b15a 0%,#c99a3f 14%,#d84a2c 18%,#c8372a 100%)}
.jar-mild{left:498px;top:470px;width:225px;height:370px;z-index:1;background:linear-gradient(180deg,#e1c16a 0%,#c9a04a 15%,#a6c24e 19%,#8fae3a 100%)}
.jar-medium{left:700px;top:498px;width:200px;height:340px;background:linear-gradient(180deg,#d7b15a 0%,#c99a3f 14%,#ee8d2c 18%,#e06a26 100%)}

.featured-title{left:126px;top:980px;font-size:48px;font-weight:600;color:var(--ink);line-height:1.1}
.featured-rule{left:126px;top:1050px;width:333px;height:3px;background:var(--ink)}
.featured-sub{left:127px;top:1072px;font-size:32px;font-weight:500;color:var(--red);line-height:1.2}
.featured-copy{left:126px;top:1133px;width:400px;font-size:15.5px;line-height:24px;color:var(--ink)}
.featured-btn{left:128px;top:1323px;width:142px;height:53px;font-size:20px}
.featured-img{left:674px;top:967px;width:390px;height:390px;border-radius:50%;background:radial-gradient(circle,#f7a23a 0%,#ee7a1c 70%,#e9661a 100%)}
.featured-jar{left:757px;top:1025px;width:225px;height:365px;border-radius:40px 40px 50px 50px;background:linear-gradient(180deg,#e1c16a 0%,#c9a04a 14%,#f0a23a 18%,#e56f22 100%);box-shadow:0 16px 22px rgba(0,0,0,.2)}

.review-band{left:0;top:1495px;width:1200px;height:670px}
.review-card{left:163px;top:1637px;width:874px;height:406px;background:var(--white);border-radius:6px}
.review-title{left:0;top:40px;width:874px;text-align:center;font-size:42px;font-weight:600;color:var(--ink);line-height:1.1}
.review{top:133px;width:190px}
.stars{display:flex;gap:2px;margin-bottom:18px}
.review q{display:block;font-weight:500;font-size:14.5px;line-height:20px;color:var(--ink);margin-bottom:4px}
.review p{font-size:14.5px;line-height:20px;color:var(--muted)}
.review .by{position:absolute;top:195px;font-weight:500;font-size:14.5px;color:var(--ink)}
.divider{top:133px;width:1px;height:208px;background:#e3e3e3}

.recipes-title{left:0;top:2238px;width:1200px;text-align:center;font-size:42px;font-weight:600;color:var(--ink);line-height:1.1}
.recipes-rule{left:538px;top:2298px;width:124px;height:3px;background:var(--ink)}
.recipe-img{top:2338px;width:296px;height:355px;border-radius:20px}
.recipe-name{top:2706px;width:296px;text-align:center;font-family:"Oswald",sans-serif;font-weight:500;font-size:18px;line-height:24px;color:var(--ink);text-transform:uppercase}
.arrow{top:2495px;width:44px;height:44px}

.insta-band{left:0;top:2876px;width:1200px;height:197px;background:var(--red)}
.insta-text{left:0;top:2948px;width:1200px;text-align:center;color:var(--white);font-size:38px;font-weight:500;line-height:1.2}
.insta-rule{left:309px;top:3006px;width:582px;height:3px;background:var(--white)}

.footer-mail{left:128px;top:3197px}
.footer-contact{left:188px;top:3194px;font-family:"Oswald",sans-serif;font-weight:500;font-size:16px;line-height:24px;color:var(--ink);text-transform:uppercase}
.footer-brand{left:470px;top:3185px;width:270px;text-align:center;font-family:"Oswald",sans-serif;font-weight:600;font-size:60px;line-height:1.2;color:var(--red)}
.footer-links{font-family:"Oswald",sans-serif;font-weight:500;font-size:16px;color:var(--ink);text-transform:uppercase}
.copyright{left:0;top:3333px;width:1200px;text-align:center;font-size:15px;line-height:25px;color:var(--ink);text-transform:uppercase}
</style>
</head>
<body>

<header class="abs site-header">
  <div class="abs brand">Rio Dorado</div>
  <div class="abs account">MY ACCOUNT
    <svg width="22" height="22" viewBox="0 0 22 22" fill="none" stroke="#111" stroke-width="1.8"><circle cx="11" cy="7" r="5"/><path d="M2 21c1-5 5-7 9-7s8 2 9 7"/></svg>
  </div>
  <div class="abs order-btn">
    <svg width="20" height="20" viewBox="0 0 20 20" fill="none" stroke="#fff" stroke-width="1.8"><rect x="2" y="6" width="16" height="12" rx="2"/><path d="M6 6V5a4 4 0 0 1 8 0v1"/></svg>ORDER ONLINE
  </div>
  <nav class="abs main-nav">
    <span class="active">HOME</span><span>PRODUCT</span><span>WHERE TO BUY</span><span>RECIPE</span><span>ABOUT</span><span>REVIEW</span><span>CONTACT</span>
  </nav>
</header>

<section>
  <div class="abs hero" role="img" aria-label="Close-up photo of tacos with salsa, radish and lime"></div>
  <div class="abs hero-shade"></div>
  <svg class="abs hero-fade" viewBox="0 0 1200 300" preserveAspectRatio="none">
    <defs><linearGradient id="fade" x1="0" y1="0" x2="0" y2="1"><stop offset="0" stop-color="#f6f0e6" stop-opacity=".9"/><stop offset=".35" stop-color="#f6f0e6"/></linearGradient></defs>
    <path d="M0 22 L25 40 L55 30 L90 52 L130 44 L175 70 L215 58 L260 78 L300 66 L340 86 L900 88 L940 70 L980 84 L1020 60 L1060 72 L1100 50 L1140 58 L1170 36 L1200 44 L1200 300 L0 300 Z" fill="url(#fade)"/>
  </svg>
  <div class="abs chili chili-left" role="img" aria-label="White chili pepper illustration"></div>
  <div class="abs chili chili-right" role="img" aria-label="White chili pepper illustration"></div>
  <div class="abs head-font hero-kicker">Welcome to Rio Dorado</div>
  <h1 class="abs head-font hero-title">Spice up your meals!</h1>
  <div class="abs btn hero-btn">Shop now</div>
  <div class="abs jar jar-hot" role="img" aria-label="Habanero salsa jar, hot"></div>
  <div class="abs jar jar-medium" role="img" aria-label="All natural salsa jar, medium"></div>
  <div class="abs jar jar-mild" role="img" aria-label="Verde salsa jar, mild"></div>
</section>

<section>
  <h2 class="abs head-font featured-title">Featured Product</h2>
  <div class="abs featured-rule"></div>
  <h3 class="abs head-font featured-sub">All Natural Salsa</h3>
  <p class="abs featured-copy">Lorem ipsum dolor sit amet, consectetur adipisci ng elit, sed do eiusmod tempor incididunt ut labore et dolore magna aliqua. Quis ipsum suspendisse ultrices gravida. Risus commodo viverra maecenas accumsan lacus vel faci Risus commodo viverra maecenas accumsan lacusagna aliquauis ipsum suspendisse ultrices gravida.</p>
  <div class="abs btn featured-btn">Shop now</div>
  <div class="abs featured-img" role="img" aria-label="Orange sunburst circle behind the product"></div>
  <div class="abs featured-jar" role="img" aria-label="All natural salsa jar"></div>
</section>

<section>
  <svg class="abs review-band" viewBox="0 0 1200 670" preserveAspectRatio="none">
    <path d="M0 22 L40 18 L90 28 L150 16 L210 26 L280 12 L350 24 L420 10 L500 22 L580 8 L660 20 L740 10 L820 24 L900 12 L980 22 L1060 8 L1130 18 L1200 6 L1200 600 L1150 590 L1090 606 L1020 594 L950 612 L880 598 L800 616 L720 602 L640 620 L560 604 L480 618 L400 602 L320 616 L240 600 L160 612 L80 598 L0 608 Z" fill="var(--red)"/>
  </svg>
  <div class="abs review-card">
    <h2 class="abs head-font review-title">Reviews</h2>
    <div class="abs review" style="left:77px">
      <div class="stars"><svg width="72" height="12" viewBox="0 0 72 12"><g fill="var(--star)"><path id="s" d="M6 0l1.8 3.8 4.2.5-3.1 2.9.8 4.1L6 9.3 2.3 11.3l.8-4.1L0 4.3l4.2-.5z"/><use href="#s" x="14.5"/><use href="#s" x="29"/><use href="#s" x="43.5"/><use href="#s" x="58"/></g></svg></div>
      <q>Very good, and I’m a salsa snob!</q>
      <p>Lorem ipsum dolor lotsit amet, consectetur adipis cing elit, sed do eiusmod tempor incididunt ut lab ore et dolore maa.</p>
      <div class="by">-Dara Quill</div>
    </div>
    <div class="abs divider" style="left:297px"></div>
    <div class="abs review" style="left:346px">
      <div class="stars"><svg width="72" height="12" viewBox="0 0 72 12"><g fill="var(--star)"><use href="#s"/><use href="#s" x="14.5"/><use href="#s" x="29"/><use href="#s" x="43.5"/><use href="#s" x="58"/></g></svg></div>
      <q>Awesome taste, fresh.</q>
      <p>Lorem ipsum dolor lotsit amet, consectetur adipis cing elit, sed do eiusmod tempor incididunt ut lab ore et dolore maa.</p>
      <div class="by">-Dara Quill</div>
    </div>
    <div class="abs divider" style="left:567px"></div>
    <div class="abs review" style="left:615px">
      <div class="stars"><svg width="72" height="12" viewBox="0 0 72 12"><g fill="var(--star)"><use href="#s"/><use href="#s" x="14.5"/><use href="#s" x="29"/><use href="#s" x="43.5"/><use href="#s" x="58"/></g></svg></div>
      <q>Really good flavor.</q>
      <p>Lorem ipsum dolor lotsit amet, consectetur adipis cing elit, sed do eiusmod tempor incididunt ut lab ore et dolore maa.</p>
      <div class="by">-Dara Quill</div>
    </div>
  </div>
</section>

<section>
  <h2 class="abs head-font recipes-title">Recipes</h2>
  <div class="abs recipes-rule"></div>
  <svg class="abs arrow" style="left:49px" viewBox="0 0 44 44" fill="none" stroke="#111" stroke-width="2"><circle cx="22" cy="22" r="20.5"/><path d="M25 14l-8 8 8 8"/></svg>
  <svg class="abs arrow" style="left:1105px" viewBox="0 0 44 44" fill="none" stroke="#111" stroke-width="2"><circle cx="22" cy="22" r="20.5"/><path d="M19 14l8 8-8 8"/></svg>
  <div class="abs recipe-img" style="left:128px;background:linear-gradient(160deg,#b98a5a,#c9552a 60%,#d8892f)" role="img" aria-label="Spoonful of one pot Mexican beef and rice with melted cheese"></div>
  <div class="abs recipe-img" style="left:453px;background:linear-gradient(160deg,#7a5a48,#6e4650 50%,#3fb6c9)" role="img" aria-label="Bowls of black bean and salsa soup with cilantro"></div>
  <div class="abs recipe-img" style="left:777px;background:linear-gradient(160deg,#2f4a2a,#e0b060 50%,#26337a)" role="img" aria-label="Baked chicken with salsa and sour cream on a blue plate"></div>
  <div class="abs recipe-name" style="left:128px">One pot Mexican<br>beef and rice</div>
  <div class="abs recipe-name" style="left:453px">Rio Dorado’s black bean<br>and salsa soup</div>
  <div class="abs recipe-name" style="left:777px">Baked chicken with salsa<br>and sour cream</div>
</section>

<section>
  <div class="abs insta-band"></div>
  <div class="abs head-font insta-text">Follow riodoradosalsa’s on Instagram</div>
  <div class="abs insta-rule"></div>
</section>

<footer>
  <svg class="abs footer-mail" width="46" height="34" viewBox="0 0 46 34" fill="none" stroke="var(--red)" stroke-width="2.5"><rect x="2" y="2" width="42" height="30"/><path d="M2 2l21 17L44 2M2 32l15-14M44 32L29 18"/></svg>
  <div class="abs footer-contact">Email address:<br>support@riodoradosalsa.example</div>
  <div class="abs footer-brand">Rio Dorado</div>
  <div class="abs footer-links" style="left:860px;top:3177px">Product</div>
  <div class="abs footer-links" style="left:860px;top:3218px">Where to buy</div>
  <div class="abs footer-links" style="left:860px;top:3258px">Recipe</div>
  <div class="abs footer-links" style="left:1003px;top:3177px">About</div>
  <div class="abs footer-links" style="left:1003px;top:3218px">Review</div>
  <div class="abs footer-links" style="left:1003px;top:3258px">Contact</div>
  <div class="abs copyright">© 2025 © Rio Dorado Salsa.<br>All rights reserved. Privacy policy</div>
</footer>

</body>
</html>
```